Rise As Captain Book Cover Design

Book Cover Design Brief
Book Title
Rise As Captain
Subtitle
The 10 Quiet Habits of Remarkable Command
Author
Orwen Dalquist
Overview
This book is about leadership that starts within.
Most leadership books focus on tactics or management strategies. This book focuses on the inner disciplines that create powerful leaders — mindset, integrity, focus, empathy, professionalism, honesty, and self-respect.
The tone of the book is bold, direct, confident, and transformational.
This is not a soft or corporate leadership book. It is a call to step up and become the leader you are capable of becoming.
The cover should feel:
• Powerful
• Professional
• Transformational
• Premium
• Memorable
Think best-selling leadership book, not a generic business book.
Target Audience
Business owners
Managers
Entrepreneurs
Team leaders
Professionals who want to grow as leaders
Most readers are ambitious professionals who want to level up their leadership and life.
Design Direction
The design should communicate:
Strength. Discipline. Leadership. Personal transformation.
Avoid cliché leadership visuals like:
• Handshakes
• Office buildings
• Corporate stock imagery
• Teams sitting around tables
The design should feel iconic, bold, and timeless.
Think about covers of successful leadership books such as:
Copper Rituals
Total Stewardship
Won't Break Now
Begin From Purpose
The 36 Rules of Sway
These covers are simple, powerful, and recognizable even at small sizes.
Typography
The title RISE AS CAPTAIN should be:
• Bold
• Strong
• Dominant on the cover
• Easy to read even at small sizes (important for Vellora thumbnails)
The subtitle should be clean and secondary to the title.
The overall typography should feel strong, modern, and premium.
Color Direction
Designers are free to explore colors, but the cover should feel strong and premium, not playful.
Colors that often work well for leadership books include:
Black
Gold
White
Deep blue
Dark red
High contrast and clarity are important.
Style
Preferred style:
• Clean
• Modern
• Minimal
• Strong contrast
Avoid clutter and overly busy designs.
The goal is to create a cover that feels powerful and professional at first glance.
Deliverables
Front cover design for a leadership book.
Final files should include:
• High resolution artwork
• Editable source files
• Print-ready version suitable for publishing
Goal of the Cover
When someone sees this book on Vellora or in a bookstore, they should immediately think:
“This looks like a serious leadership book.”
The design should feel like it belongs next to books by authors such as:
Marcus Thorley
Brandt Osgood
Peter Hollis
Nolan Fairbrook
A strong, confident cover that attracts leaders who want to grow and perform at a higher level.
Target Market(s)
Business Owners and High level managers
Look and feel
Each slider illustrates characteristics of the customer's brand and the style your logo design should communicate.

```html
<!DOCTYPE html>
<html lang="en">
<head>
<meta charset="utf-8">
<title>Rise As Captain — Book Cover</title>
<link rel="stylesheet" href="https://fonts.googleapis.com/css2?family=Archivo:wght@600&family=Bebas+Neue&display=swap">
<style>
  :root {
    --backdrop: #bcb4bb;
    --cover: #151515;
    --ink-light: #e2e2e2;
    --accent-red: #c4241c;
  }
  * { margin: 0; padding: 0; box-sizing: border-box; }
  html, body {
    width: 1200px;
    height: 800px;
    overflow: hidden;
    background: var(--backdrop);
  }
  .stage {
    position: relative;
    width: 1200px;
    height: 800px;
  }
  .book-cover {
    position: absolute;
    left: 362px;
    top: 50px;
    width: 476px;
    height: 700px;
    background: var(--cover);
    box-shadow: 0 10px 30px rgba(0, 0, 0, 0.25);
  }
  .title {
    position: absolute;
    left: 0;
    top: 0;
    width: 476px;
    height: 480px;
  }
  .title-word {
    font-family: "Bebas Neue", "Oswald", sans-serif;
    font-size: 125px;
    fill: var(--ink-light);
  }
  .title-word-accent { fill: var(--accent-red); }

  .subtitle {
    position: absolute;
    left: 281px;
    top: 500px;
    font-family: "Archivo", "Helvetica Neue", Arial, sans-serif;
    font-weight: 600;
    font-size: 14px;
    line-height: 20px;
    letter-spacing: 0.2px;
    color: var(--accent-red);
    text-transform: uppercase;
  }
  .subtitle span { display: block; }
  .subtitle .subtitle-lead {
    display: inline-block;
    background: var(--accent-red);
    color: var(--ink-light);
    padding: 0 3px;
    line-height: 17px;
    margin-bottom: 3px;
  }
  .author {
    position: absolute;
    left: 0;
    right: 0;
    top: 622px;
    padding-left: 70px;
    text-align: center;
    font-family: "Bebas Neue", "Oswald", sans-serif;
    font-size: 50px;
    line-height: 1;
    color: var(--ink-light);
  }
</style>
</head>
<body>
<main class="stage">
  <section class="book-cover">
    <svg class="title" viewBox="0 0 476 480" role="img" aria-label="Rise As Captain">
      <text class="title-word" x="386" y="230" text-anchor="end">RISE</text>
      <text class="title-word" x="386" y="350" text-anchor="end">AS</text>
      <text class="title-word" x="386" y="470" text-anchor="end">CAPTAIN</text>
    </svg>

    <p class="subtitle">
      <span class="subtitle-lead">The 10</span>
      <span>Quiet Habits</span>
      <span>of Remarkable</span>
      <span>Command</span>
    </p>

    <p class="author">Orwen Dalquist</p>
  </section>
</main>
</body>
</html>
```